Perfume packaging design

We are a company producing perfumery and deodorants in the upper mass market segment (semi-selective). We need a packaging design for our new fragrance for women called Moon Petal. You will find attached a picture of the chosen bottle and cap along with specification.

The fragrance is modern and delicate. It is sweet with floral accent and notes of mandarin, rose, peach.

Suitable for evening perfume as well as casual daily.

Looking for:
1. logo - "Moon Petal" on bottle and packaging
2. Color of the perfume
3. Design of the carton box

Product is 100ml eau de perfume for women.

Target Market(s)

Target market is Eastern Europe and middle east

Women
Age 30-45
Price range - semi-selective
Sales channels - perfumeries, drug stores and online

Industry/Entity Type

It Company

Requirements
Must have
• Packaging - carton
Perfume should be colored
Embosing
Nice to have
• Golden hot stamping or other golden element

```html
<!DOCTYPE html>
<html lang="en">
<head>
<meta charset="utf-8">
<title>Moon Petal – Eau de Perfume Packaging</title>
<link href="https://fonts.googleapis.com/css2?family=Pinyon+Script&family=Jura:wght@500;600&family=Open+Sans:wght@400&display=swap" rel="stylesheet">
<style>
  :root {
    --ink-black: #0a0508;
    --plum-deep: #2a1326;
    --plum-mid: #5a2c55;
    --orchid-glow: #a65e9b;
    --violet-liquid: #b13fd0;
    --violet-dark: #6d1f92;
    --box-night: #12051f;
    --box-violet: #4a1a8a;
    --box-magenta: #7a2a9e;
    --glass: rgba(235, 235, 245, 0.55);
    --white: #ffffff;
    --mark-lilac: #a774e6;
  }
  * { margin: 0; padding: 0; box-sizing: border-box; }
  html, body { width: 1200px; height: 900px; overflow: hidden; background: var(--ink-black); }
  .board {
    position: relative;
    width: 1200px;
    height: 900px;
    overflow: hidden;
    background:
      radial-gradient(ellipse 760px 560px at 260px 920px, var(--orchid-glow) 0%, var(--plum-mid) 45%, transparent 100%),
      linear-gradient(135deg, var(--ink-black) 0%, var(--ink-black) 25%, var(--plum-deep) 60%, var(--plum-mid) 100%);
  }
  .brand-mark {
    position: absolute;
    top: 128px;
    left: 0;
    width: 1200px;
    display: flex;
    justify-content: center;
    align-items: center;
    gap: 12px;
  }
  .brand-mark__dot {
    width: 14px; height: 14px; border-radius: 50%;
    background: var(--mark-lilac);
  }
  .brand-mark__name {
    font-family: "Pinyon Script", cursive;
    font-size: 40px;
    color: var(--mark-lilac);
    line-height: 1;
  }
  /* Bottle */
  .bottle { position: absolute; left: 220px; top: 420px; width: 300px; height: 365px; }
  .bottle__cap {
    position: absolute; left: 50px; top: 0; width: 152px; height: 152px;
    border-radius: 10px 10px 4px 4px;
    background: linear-gradient(90deg, rgba(200,200,210,0.35), rgba(245,245,250,0.75) 40%, rgba(190,190,205,0.4));
    border: 1px solid rgba(255,255,255,0.35);
  }
  .bottle__body {
    position: absolute; left: 0; top: 148px; width: 300px; height: 217px;
    border-radius: 6px;
    background: linear-gradient(90deg, var(--glass), rgba(230,230,240,0.2) 12%, transparent 14%),
                linear-gradient(180deg, var(--glass) 0%, var(--glass) 10%, var(--violet-liquid) 12%, var(--violet-dark) 55%, var(--violet-liquid) 88%, var(--glass) 92%);
  }
  .bottle__label {
    position: absolute; left: 0; top: 192px; width: 300px; text-align: center; color: var(--white);
  }
  .label-name { font-family: "Pinyon Script", cursive; font-size: 40px; line-height: 1; }
  .label-type { font-family: "Jura", sans-serif; font-weight: 600; font-size: 12px; letter-spacing: 0.5px; margin-top: 14px; line-height: 1.6; }
  .label-volume { font-family: "Open Sans", sans-serif; font-size: 11px; margin-top: 38px; }
  /* Carton */
  .carton {
    position: absolute; left: 650px; top: 298px; width: 396px; height: 509px;
    background:
      linear-gradient(160deg, transparent 30%, rgba(122,42,158,0.6) 45%, transparent 60%),
      linear-gradient(20deg, var(--box-night) 10%, var(--box-violet) 40%, var(--box-night) 70%, var(--box-magenta) 100%);
    color: var(--white);
    text-align: center;
  }
  .carton__name { position: absolute; top: 130px; left: 0; width: 100%; font-family: "Pinyon Script", cursive; font-size: 58px; line-height: 1.1; }
  .carton__type { position: absolute; top: 228px; left: 0; width: 100%; font-family: "Jura", sans-serif; font-weight: 600; font-size: 18px; letter-spacing: 0.8px; line-height: 1.7; }
  .carton__volume { position: absolute; top: 462px; left: 0; width: 100%; font-family: "Open Sans", sans-serif; font-size: 19px; }
</style>
</head>
<body>
<main class="board">
  <header class="brand-mark">
    <span class="brand-mark__dot"></span>
    <span class="brand-mark__name">Moon Petal</span>
  </header>

  <figure class="bottle">
    <div class="bottle__cap" role="img" aria-label="Clear faceted glass cap of the perfume bottle"></div>
    <div class="bottle__body" role="img" aria-label="Square glass bottle filled with violet perfume"></div>
    <div class="bottle__label">
      <div class="label-name">Moon Petal</div>
      <div class="label-type">eau de perfume<br>for women</div>
      <div class="label-volume">100ml</div>
    </div>
  </figure>

  <section class="carton" role="img" aria-label="Carton box front: deep violet night sky with scattered sparkling stars">
    <div class="carton__name">Moon Petal</div>
    <div class="carton__type">eau de perfume<br>for women</div>
    <div class="carton__volume">100ml</div>
  </section>
</main>
</body>
</html>
```